Wren's Hearth Support Business Card

Business card design
Font must be in Poppins Regular for Wren's Hearth Support
Safe Days Ahead font is Alex Brush

Colour must be Hex #910E2B
RGB 145-14-43
Pantone 7427 C
We want the card editable
On the front please include
Name eg Mavis Dunleavy
Position eg Clinical Care Manager
Phone number mobile 0473 856 342
Phone 08 7394 2650
Email : mavis@wrenshearthsupport.com.au
Address : Gullwing Cove, Western Australia, 6284
Website : wrenshearthsupport.com.au
Contact us today to experience the warmth, respect and personal touch of Wren's Hearth Support.

Target Market(s)

35+

Industry/Entity Type

aged care / community

Contact Information for Business Card

see project description

Requirements
Must have
• Colours, logos and fonts as detailed and uploaded

```html
<!DOCTYPE html>
<html lang="en">
<head>
<meta charset="utf-8">
<title>Wren's Hearth Support – Business Card</title>
<link href="https://fonts.googleapis.com/css2?family=Alex+Brush&family=Poppins:wght@400;600&display=swap" rel="stylesheet">
<style>
  :root {
    --brand-red: #910E2B;
    --ink: #1e1e1e;
    --card-paper: #f3f2f0;
    --backdrop: #d0d5d5;
  }
  * { box-sizing: border-box; margin: 0; padding: 0; }
  html, body { width: 1200px; height: 881px; overflow: hidden; }
  body {
    background: var(--backdrop);
    font-family: "Poppins", sans-serif;
    color: var(--ink);
    position: relative;
  }
  .card {
    position: absolute;
    top: 286px;
    width: 540px;
    height: 309px;
    background: var(--card-paper);
    border-bottom: 4px solid var(--brand-red);
    box-shadow: 0 12px 28px rgba(0,0,0,0.14);
  }
  .card--details { left: 40px; }
  .card--brand { left: 620px; }

  /* Details side */
  .person {
    position: absolute;
    right: 285px;
    top: 96px;
    text-align: right;
  }
  .person__name {
    font-weight: 600;
    font-size: 23px;
    color: var(--brand-red);
    line-height: 1.2;
    white-space: nowrap;
  }
  .person__role {
    font-size: 14px;
    line-height: 1.4;
    white-space: nowrap;
  }
  .divider {
    position: absolute;
    left: 270px;
    top: 92px;
    width: 1.5px;
    height: 122px;
    background: var(--brand-red);
  }
  .contact {
    position: absolute;
    left: 284px;
    top: 92px;
    list-style: none;
    font-size: 12px;
    line-height: 1.55;
  }
  .contact__item { display: flex; align-items: center; gap: 6px; white-space: nowrap; }
  .contact__item--address { padding-left: 16px; display: block; }
  .contact__icon { width: 10px; height: 10px; fill: var(--brand-red); flex: none; }
  .invite {
    position: absolute;
    left: 0; right: 0;
    bottom: 22px;
    text-align: center;
    font-size: 10px;
  }

  /* Brand side */
  .lockup {
    position: absolute;
    left: 58px;
    top: 88px;
    display: flex;
    align-items: center;
    gap: 18px;
  }
  .lockup__ring {
    width: 104px; height: 104px;
    border: 6px solid var(--brand-red);
    border-radius: 50%;
    flex: none;
  }
  .lockup__name {
    font-weight: 400;
    font-size: 40px;
    line-height: 1.02;
    color: var(--brand-red);
  }
  .tagline {
    position: absolute;
    left: 180px;
    top: 210px;
    font-family: "Alex Brush", cursive;
    font-size: 34px;
    color: var(--brand-red);
    white-space: nowrap;
  }
</style>
</head>
<body>

<section class="card card--details" aria-label="Contact details side">
  <div class="person">
    <p class="person__name">eg Mavis Dunleavy</p>
    <p class="person__role">eg Clinical Care Manager</p>
  </div>
  <div class="divider"></div>
  <ul class="contact">
    <li class="contact__item contact__item--address">Gullwing Cove,<br>Western Australia, 6284</li>
    <li class="contact__item">
      <svg class="contact__icon" viewBox="0 0 10 10"><path d="M2.5 0h5a1 1 0 0 1 1 1v8a1 1 0 0 1-1 1h-5a1 1 0 0 1-1-1V1a1 1 0 0 1 1-1zm.3 1.2v6.6h4.4V1.2z"/></svg>
      0473 856 342
    </li>
    <li class="contact__item">
      <svg class="contact__icon" viewBox="0 0 10 10"><path d="M0 3.2C1.5 1.4 3.2.8 5 .8s3.5.6 5 2.4L8.6 4.5 7 3.6V2.6C5.7 2.2 4.3 2.2 3 2.6v1L1.4 4.5zM2 5.2h6l1 4H1z"/></svg>
      08 7394 2650
    </li>
    <li class="contact__item">
      <svg class="contact__icon" viewBox="0 0 10 10"><path d="M0 2h10v.8L5 5.6 0 2.8zm0 1.8 5 2.8 5-2.8V8H0z"/></svg>
      mavis@wrenshearthsupport.com.au
    </li>
    <li class="contact__item">
      <svg class="contact__icon" viewBox="0 0 10 10"><circle cx="5" cy="5" r="5"/><path d="M0 5h10M5 0c-2 2.5-2 7.5 0 10M5 0c2 2.5 2 7.5 0 10" stroke="#f3f2f0" stroke-width=".8" fill="none"/></svg>
      www.wrenshearthsupport.com.au
    </li>
  </ul>
  <p class="invite">Contact us today to experience the warmth, respect and personal touch of Wren's Hearth Support</p>
</section>

<section class="card card--brand" aria-label="Brand side">
  <div class="lockup">
    <div class="lockup__ring"></div>
    <p class="lockup__name">Wren's Hearth<br>Support</p>
  </div>
  <p class="tagline">Safe Days Ahead</p>
</section>

</body>
</html>
```